Updated business card

I would like to change the picture on the existing design. Please use the attached photo. Remove my last name from the logo and have that appear (just my first name with the lock symbol [trademarked]) appear horizontally or vertically? on the front of the card. My company information has changed on the back of the card. It should be "Lantern" instead of "Harborline 88 Oakmont Realty", 4720 Fenwick Blvd. Arlington, VA 22207 is the new address. The Harborline 88 Oakmont logo should be replaced with the Lantern logo which is attached as well. I am using Pixo cards with the rounded edges for printing so the size is larger than the typically business card. The colors should remain consistent with what I have but can be used differently.

```html
<!DOCTYPE html>
<html lang="en">
<head>
<meta charset="utf-8">
<title>Marisol Keene – Business Cards</title>
<link rel="stylesheet" href="https://fonts.googleapis.com/css2?family=Montserrat:wght@400;500;600;700&family=Yellowtail&display=swap">
<style>
  :root {
    --backdrop: #232323;
    --magenta: #d4118a;
    --ink: #1b1b1b;
    --white: #ffffff;
    --photo-light: #d9d4d0;
    --photo-dark: #8a4f2c;
    --band: #0d0d0d;
  }
  * { margin: 0; padding: 0; box-sizing: border-box; }
  html, body { width: 1200px; height: 1000px; overflow: hidden; }
  body {
    position: relative;
    background: var(--backdrop);
    font-family: "Montserrat", Arial, sans-serif;
    color: var(--ink);
  }
  .card { position: absolute; box-shadow: 0 6px 18px rgba(0,0,0,.55); }

  /* Front card */
  .card-front { left: 28px; top: 172px; width: 662px; height: 492px; background: var(--magenta); }
  .portrait {
    position: absolute; left: 0; top: 0; width: 330px; height: 360px;
    background: linear-gradient(160deg, var(--photo-light) 0%, #c9b3a4 45%, var(--photo-dark) 100%);
  }
  .brand-band {
    position: absolute; left: 0; top: 360px; width: 330px; height: 132px;
    background: var(--band); color: var(--white); text-align: center;
  }
  .brand-name {
    position: absolute; left: 0; right: 0; top: 28px;
    font-size: 32px; font-weight: 400; letter-spacing: 1px;
    display: flex; align-items: center; justify-content: center; gap: 10px;
  }
  .brand-dot { width: 14px; height: 14px; border-radius: 50%; background: var(--magenta); }
  .brand-tagline {
    position: absolute; left: 0; right: 0; top: 80px;
    font-size: 16px; font-weight: 400; letter-spacing: .3px;
  }

  /* Contact panels */
  .contact { position: absolute; text-align: center; }
  .front-contact { left: 330px; top: 0; width: 332px; height: 492px; }
  .back-contact { left: 0; top: 0; width: 437px; height: 651px; }
  .contact > * { position: absolute; left: 0; right: 0; }
  .name { font-weight: 700; letter-spacing: .4px; }
  .title { font-family: "Yellowtail", cursive; }
  .credential { font-weight: 400; }
  .icon { margin: 0 auto; display: block; }
  .detail { font-weight: 400; }
  .address { font-weight: 700; line-height: 1.25; }
  .brokerage { display: flex; justify-content: center; align-items: center; }
  .brokerage-name { font-weight: 500; letter-spacing: 2px; color: var(--ink); }
  .housing-badge { background: var(--ink); }

  .front-contact .name { top: 46px; font-size: 14px; }
  .front-contact .title { top: 64px; font-size: 19px; }
  .front-contact .credential { top: 90px; font-size: 12.5px; }
  .front-contact .i-mail { top: 129px; }
  .front-contact .d-mail { top: 164px; font-size: 14.5px; }
  .front-contact .i-phone { top: 200px; }
  .front-contact .d-phone { top: 237px; font-size: 14.5px; }
  .front-contact .i-web { top: 273px; }
  .front-contact .d-web { top: 310px; font-size: 14.5px; }
  .front-contact .address { top: 360px; font-size: 12px; }
  .front-contact .brokerage { top: 414px; gap: 48px; }
  .front-contact .brokerage-name { font-size: 14px; }
  .front-contact .housing-badge { width: 44px; height: 40px; }

  /* Back card */
  .card-back { left: 719px; top: 172px; width: 437px; height: 651px; background: var(--magenta); }
  .back-contact .name { top: 61px; font-size: 18px; }
  .back-contact .title { top: 84px; font-size: 25px; }
  .back-contact .credential { top: 118px; font-size: 16px; }
  .back-contact .i-mail { top: 169px; }
  .back-contact .d-mail { top: 215px; font-size: 20px; }
  .back-contact .i-phone { top: 263px; }
  .back-contact .d-phone { top: 311px; font-size: 20px; }
  .back-contact .i-web { top: 359px; }
  .back-contact .d-web { top: 407px; font-size: 20px; }
  .back-contact .address { top: 477px; font-size: 16px; }
  .back-contact .brokerage { top: 546px; gap: 50px; }
  .back-contact .brokerage-name { font-size: 18px; }
  .back-contact .housing-badge { width: 58px; height: 52px; }
</style>
</head>
<body>

<section class="card card-front">
  <div class="portrait" role="img" aria-label="Portrait photograph of the realtor"></div>
  <div class="brand-band">
    <div class="brand-name"><span class="brand-dot"></span><span>MARISOL</span></div>
    <div class="brand-tagline">Homes Thoughtfully Staged.</div>
  </div>
  <div class="contact front-contact">
    <div class="name">MARISOL KEENE, J.D., LL.M.</div>
    <div class="title">Realtor</div>
    <div class="credential">Accredited Staging Professional</div>
    <svg class="icon i-mail" width="30" height="30" viewBox="0 0 40 40"><circle cx="20" cy="20" r="18" fill="none" stroke="#fff" stroke-width="2.6"/><rect x="10.5" y="13" width="19" height="14" rx="1.5" fill="#fff"/><path d="M11 14l9 7 9-7" fill="none" stroke="#d4118a" stroke-width="1.8"/></svg>
    <div class="detail d-mail">Marisol@MarisolKeene.com</div>
    <svg class="icon i-phone" width="30" height="30" viewBox="0 0 40 40"><circle cx="20" cy="20" r="18" fill="none" stroke="#fff" stroke-width="2.6"/><path d="M14 10.5c1.2-.8 2.2-.6 2.8.4l2 3.3c.5.9.3 1.8-.5 2.4l-1.4 1c.9 2.4 2.5 4.5 4.6 5.8l1.1-1.3c.7-.7 1.6-.8 2.4-.2l3.1 2.3c.9.7 1 1.8.1 2.8-1.6 1.8-3.4 2.3-5.6 1.2-5.1-2.5-8.8-7-9.9-12.5-.4-2 .1-3.6 1.3-4.4z" fill="#fff"/></svg>
    <div class="detail d-phone">202.555.0148</div>
    <svg class="icon i-web" width="30" height="30" viewBox="0 0 40 40"><circle cx="20" cy="20" r="18" fill="none" stroke="#fff" stroke-width="2.6"/><circle cx="13.5" cy="26.5" r="2.4" fill="#fff"/><path d="M12 19a9 9 0 0 1 9 9M12 12.5a15.5 15.5 0 0 1 15.5 15.5" fill="none" stroke="#fff" stroke-width="2.6" stroke-linecap="round"/></svg>
    <div class="detail d-web">MarisolKeene.com</div>
    <div class="address">4720 Fenwick Blvd.<br>Arlington, VA 22207</div>
    <div class="brokerage"><span class="brokerage-name">LANTERN</span><span class="housing-badge" role="img" aria-label="Equal housing badge"></span></div>
  </div>
</section>

<section class="card card-back">
  <div class="contact back-contact">
    <div class="name">MARISOL KEENE, J.D., LL.M.</div>
    <div class="title">Realtor</div>
    <div class="credential">Accredited Staging Professional</div>
    <svg class="icon i-mail" width="40" height="40" viewBox="0 0 40 40"><circle cx="20" cy="20" r="18" fill="none" stroke="#fff" stroke-width="2.6"/><rect x="10.5" y="13" width="19" height="14" rx="1.5" fill="#fff"/><path d="M11 14l9 7 9-7" fill="none" stroke="#d4118a" stroke-width="1.8"/></svg>
    <div class="detail d-mail">Marisol@MarisolKeene.com</div>
    <svg class="icon i-phone" width="40" height="40" viewBox="0 0 40 40"><circle cx="20" cy="20" r="18" fill="none" stroke="#fff" stroke-width="2.6"/><path d="M14 10.5c1.2-.8 2.2-.6 2.8.4l2 3.3c.5.9.3 1.8-.5 2.4l-1.4 1c.9 2.4 2.5 4.5 4.6 5.8l1.1-1.3c.7-.7 1.6-.8 2.4-.2l3.1 2.3c.9.7 1 1.8.1 2.8-1.6 1.8-3.4 2.3-5.6 1.2-5.1-2.5-8.8-7-9.9-12.5-.4-2 .1-3.6 1.3-4.4z" fill="#fff"/></svg>
    <div class="detail d-phone">202.555.0148</div>
    <svg class="icon i-web" width="40" height="40" viewBox="0 0 40 40"><circle cx="20" cy="20" r="18" fill="none" stroke="#fff" stroke-width="2.6"/><circle cx="13.5" cy="26.5" r="2.4" fill="#fff"/><path d="M12 19a9 9 0 0 1 9 9M12 12.5a15.5 15.5 0 0 1 15.5 15.5" fill="none" stroke="#fff" stroke-width="2.6" stroke-linecap="round"/></svg>
    <div class="detail d-web">MarisolKeene.com</div>
    <div class="address">4720 Fenwick Blvd.<br>Arlington, VA 22207</div>
    <div class="brokerage"><span class="brokerage-name">LANTERN</span><span class="housing-badge" role="img" aria-label="Equal housing badge"></span></div>
  </div>
</section>

</body>
</html>
```